Business Card Design Project

This is the first time we use our new logo. We need a business card that we can use both on our institutional corporate relationships and also that works for our staff that deals with consumers directly.

VELUNDA is a new company dedicated to empower consumers and to provide them with the best choices for specialized health care using the latest telemedicine technology (medicine at a distance via videoconference).

We want to print this cards in high quality materials and process. We will like designs that allow us to use UV spot varnish and other techniques that will differentiate us.

We are including Two different versions of Color logos. In addition we are including white over black background logos. Those can be used replacing the black for a color.

Please note this is the first time we will be creating any corporate materials with our new logo and colors.

Target Market(s)

34+ consumers of medium high and high socioeconomic levels.

Industry/Entity Type

Health

Requirements
Must have
• Our logo on its original colors
Should not have
• Any other graphical element or design that is not our logo

```html
<!DOCTYPE html>
<html lang="en">
<head>
<meta charset="utf-8">
<title>VELUNDA business card</title>
<link href="https://fonts.googleapis.com/css2?family=Titillium+Web:wght@400;600&display=swap" rel="stylesheet">
<style>
  :root {
    --backdrop: #3a3a3c;
    --card: #1e1f22;
    --varnish: #4a4b4f;
    --brand-blue: #1f5f93;
    --accent-cyan: #1fa6dc;
    --text-light: #e4e6ea;
    --text-muted: #c2c5ca;
  }
  * { margin: 0; padding: 0; box-sizing: border-box; }
  html, body {
    width: 1200px;
    height: 900px;
    overflow: hidden;
    background: var(--backdrop);
  }
  .stage {
    position: relative;
    width: 1200px;
    height: 900px;
    font-family: "Titillium Web", sans-serif;
  }
  .card {
    position: absolute;
    top: 192px;
    width: 299px;
    height: 515px;
    background: var(--card);
    box-shadow: 0 2px 10px rgba(0, 0, 0, 0.35);
  }
  .card--front { left: 274px; }
  .card--back { left: 629px; }

  /* front: brand name in varnish tone */
  .front-name {
    position: absolute;
    left: 0;
    right: 0;
    top: 232px;
    text-align: center;
    font-size: 44px;
    font-weight: 600;
    letter-spacing: 2px;
    color: var(--varnish);
  }

  /* back: brand block */
  .brand-dot {
    position: absolute;
    left: 114px;
    top: 62px;
    width: 70px;
    height: 70px;
    border-radius: 50%;
    background: var(--accent-cyan);
  }
  .brand-name {
    position: absolute;
    left: 0;
    right: 0;
    top: 176px;
    text-align: center;
    font-size: 50px;
    font-weight: 600;
    letter-spacing: 2px;
    line-height: 1;
    color: var(--brand-blue);
  }

  .person {
    position: absolute;
    left: 29px;
    top: 313px;
  }
  .person-name {
    font-size: 23px;
    font-weight: 400;
    line-height: 1.1;
    color: var(--accent-cyan);
  }
  .person-role {
    font-size: 12.5px;
    line-height: 1.3;
    color: var(--text-muted);
  }
  .divider {
    position: absolute;
    left: 29px;
    top: 366px;
    width: 248px;
    height: 1.5px;
    background: var(--accent-cyan);
  }
  .contacts {
    position: absolute;
    left: 29px;
    top: 382px;
    font-size: 13px;
    line-height: 15px;
    color: var(--text-light);
  }
  .contact-row { display: flex; }
  .contact-label {
    width: 18px;
    font-weight: 600;
    color: var(--accent-cyan);
  }
  .contact-gap { height: 15px; }
</style>
</head>
<body>
<main class="stage">
  <section class="card card--front" aria-label="Card front">
    <p class="front-name">VELUNDA</p>
  </section>

  <section class="card card--back" aria-label="Card back">
    <div class="brand-dot" aria-hidden="true"></div>
    <p class="brand-name">VELUNDA</p>

    <div class="person">
      <p class="person-name">Daniel Moreaux</p>
      <p class="person-role">managing director</p>
    </div>
    <div class="divider"></div>

    <div class="contacts">
      <div class="contact-row"><span class="contact-label">A</span><span>48 Harlow Avenue</span></div>
      <div class="contact-row"><span class="contact-label"></span><span>Brookfield, New York 10482</span></div>
      <div class="contact-row"><span class="contact-label">P</span><span>212 604 31 27</span></div>
      <div class="contact-row"><span class="contact-label">F</span><span>212 604 31 28</span></div>
      <div class="contact-gap"></div>
      <div class="contact-row"><span class="contact-label">E</span><span>info@velunda.com</span></div>
      <div class="contact-row"><span class="contact-label">W</span><span>www.velunda.com</span></div>
    </div>
  </section>
</main>
</body>
</html>
```